a Label for a candle jar and its gift box

I would like a label that is modern minimalist for candles jars. These jars are colored as white, amber and black. I am thinking maybe foiling gold/silver background with logo only and maybe company name in different color that suits the foiling background color/s. I would like a high quality luxurious design that shows the preciousness of this candle. I am open to any ideas you might have for the design but so far I have used a logo only on the jar which I really like BUT I still feel that it is not enough branding for people when you only show them the logo so I am considering adding the business name. Again, I am open to both ideas (with logo only or logo with business name (Silken Meadow).

IMPORTANT: YOU MAY IGNORE MY DESIGN COMPLETELY AND DO YOUR OWN ONE AS LONG AS YOU KERP THE LOGO DESIGN. YOU MAY ALSO ADJUST THE LOGO A BIT TO SUIT YOUR DESIGN. - sorry im using capital letters to show importance but im not yelling :)

UPDATE: To clarify, I have uploaded a video called Corvel in the box to show what the current product look like. It is a corvel jar with a logo only and the jar box has a window that shows the jar with the logo on it and the back of that jar box has a bigger version of the label that has more details (i.e. Fragrance name and website link). So to make it clear, I would like to have two versions of the lables: 1. on the jar with minimal info (logo only or logo with the business name) 2. Bigger version of the label with more info to put on the back of the jar box - as described above. The dimensions of the jars are as per this link https://www.lunaxo-example.com.au/corvel-medium-base-and-flat-lid-amber-packed-with-lid-on/ The dimensions of the jar box as per this link https://www.lunaxo-example.com.au/corvel-medium-flat-lid-candle-box-with-window-beige/ Looking forward to some artistic productions :)

Update #2: Tues 25 Dec 18 1. I have uploaded the photo which has the logo with the name 'Silken Meadow' below it just for a reference. However, I would like the designer to modify the current font and NOT to use it as the word 'of in the phrase 'Silken Meadow' does not come out clear enough after printing. 2. I would like the designer NOT to create a design that will require a clear sticker/label for printing. 3. I have attached the photos of my current designs on the jars or the jar box just as a reference but please do NOT just use the same fonts and only change background. I am hoping to see something different and more professional than my own design :) Thank you very much!

Font styles to use
Decorative
Script

Requirements
Must have
• I would like them to fit on the three colors of the jars below - white, amber and black. Below is a link to how the jar looks like https://www.lunaxo-example.com.au/candle-making-supplies/candle-jars/corvel-candle-jars/?glassware_colour=415,443,417&glassware_size=268
Nice to have
• I would like to have a modern design which is suitable for both feminine and musculine.
Should not have
• shouldnt have so much writing on it!

```html
<!DOCTYPE html>
<html lang="en">
<head>
<meta charset="utf-8">
<title>Silken Meadow – Jar Label</title>
<link rel="stylesheet" href="https://fonts.googleapis.com/css2?family=IM+Fell+English+SC&family=Pinyon+Script&display=swap">
<style>
  :root {
    --ink: #000000;
    --bronze: #c39a6b;
    --paper: #ffffff;
    --type-dark: #1b140c;
  }
  html, body {
    margin: 0;
    padding: 0;
    overflow: hidden;
    background: var(--paper);
  }
  .label-sheet {
    position: relative;
    width: 849px;
    height: 1200px;
    background: var(--paper);
    overflow: hidden;
  }
  .stripe-band {
    position: absolute;
    left: 180px;
    width: 489px;
    display: flex;
    flex-direction: column;
  }
  .stripe-band .bar-heavy { background: var(--ink); height: 13px; }
  .stripe-band .bar-bronze-thin { background: var(--bronze); height: 4px; }
  .stripe-band .bar-fine { background: var(--ink); height: 3px; }
  .stripe-band .band-panel {
    background: var(--bronze);
    display: flex;
    align-items: center;
    justify-content: center;
    color: var(--type-dark);
    overflow: hidden;
  }
  .fragrance-band { top: 136px; }
  .fragrance-band .band-panel { height: 48px; }
  .fragrance-name {
    font-family: "Pinyon Script", cursive;
    font-size: 30px;
    letter-spacing: 6px;
    line-height: 1;
    padding-top: 4px;
    white-space: nowrap;
  }
  .brand-band { top: 689px; }
  .brand-band .bar-heavy { height: 15px; }
  .brand-band .band-panel { height: 74px; }
  .brand-title {
    font-family: "IM Fell English SC", serif;
    font-size: 30px;
    letter-spacing: 2px;
    line-height: 1;
    white-space: nowrap;
  }
  .brand-seal {
    position: absolute;
    left: 268px;
    top: 296px;
    width: 314px;
    height: 314px;
  }
  .seal-name {
    font-family: "IM Fell English SC", serif;
    font-size: 30px;
    letter-spacing: 1.5px;
    fill: var(--bronze);
  }
</style>
</head>
<body>
  <main class="label-sheet">
    <section class="stripe-band fragrance-band">
      <div class="bar-heavy"></div>
      <div class="bar-bronze-thin"></div>
      <div class="bar-fine"></div>
      <div class="band-panel"><span class="fragrance-name">Mandarin Cove</span></div>
      <div class="bar-fine"></div>
      <div class="bar-bronze-thin"></div>
      <div class="bar-heavy"></div>
    </section>

    <svg class="brand-seal" viewBox="0 0 314 314" aria-label="Silken Meadow">
      <circle cx="157" cy="157" r="156" fill="var(--ink)"/>
      <text class="seal-name" x="157" y="167" text-anchor="middle">Silken Meadow</text>
    </svg>

    <section class="stripe-band brand-band">
      <div class="bar-heavy"></div>
      <div class="bar-bronze-thin"></div>
      <div class="bar-fine"></div>
      <div class="band-panel"><span class="brand-title">Silken Meadow</span></div>
      <div class="bar-fine"></div>
      <div class="bar-bronze-thin"></div>
      <div class="bar-heavy"></div>
    </section>
  </main>
</body>
</html>
```